International Firefighter Competition Needs New Website that Looks Like It's a Global Sportin...

The Blazeguard Relay is held globally and sees thousands of firefighters competing on an obstacle course known as the toughest two minutes in sports. This year the organization received a makeover with new logo and new look of our challenge course. We also introduced the Blazeguard Relay Circuit (known as the BRC). We envision a new website that inspires our next generation of competitors! It's time to wow them visually and to make them feel that this exciting sport proudly represents them as our global heroes that protect each and every one of us in a moments notice! NOTE: Photos provided are just for you to use as placeholders. TO SEE A VIDEO OF OUR EVENT: https://clipvault-example.net/734205918

NOTE: In 2023 we sub-divided the U.S. into 5 new regions for the BRC: Blazeguard Relay Circuit. I've now added these logos in the event a designer sees a vision of integrating these.

Target Market(s)

Firefighters and Sponsors

Coding

Coded - Design and coding required

Requirements
Must have
• Rival other major sporting event websites. See attached samples.
Nice to have
• No suggestions. We truly are open to creativity.
Should not have
• Too firefighter looking. Needs to be the perfect blend of promoting our firefighters as athletes in our sport.

```html
<!DOCTYPE html>
<html lang="en">
<head>
<meta charset="utf-8">
<title>Blazeguard Relay</title>
<link href="https://fonts.googleapis.com/css2?family=Barlow:ital,wght@0,300;0,400;0,500;0,600;0,700;0,800;1,900&display=swap" rel="stylesheet">
<style>
:root{
  --navy:#1f2a44;
  --navy-deep:#161d31;
  --card:#25304c;
  --red:#d43a3e;
  --blue:#1e90d6;
  --white:#ffffff;
  --ink:#1d2e4d;
  --muted:#dfe3ec;
}
*{box-sizing:border-box;margin:0;padding:0}
html,body{width:1200px;height:2852px;overflow:hidden}
body{position:relative;font-family:"Barlow",sans-serif;color:var(--white);background:var(--navy-deep)}
section,.footer{position:absolute;left:0;width:1200px;overflow:hidden}

/* hero */
.hero{top:0;height:668px}
.hero-photo{position:absolute;inset:0;background:
  radial-gradient(ellipse at 18% 35%,#f07a1c 0%,#b5400f 22%,rgba(80,30,20,.6) 45%,transparent 65%),
  radial-gradient(ellipse at 70% 50%,#2b3a5c 0%,#141c30 60%),#0f1526}
.brand{position:absolute;display:flex;align-items:center;gap:8px;font-weight:800;font-size:20px;letter-spacing:.5px;color:var(--white);white-space:nowrap}
.brand-mark{width:18px;height:18px;border-radius:50%;background:var(--red)}
.hero .brand{left:50px;top:92px}
.nav{position:absolute;top:38px;left:651px;display:flex;gap:22px;font-size:10.5px;font-weight:700;letter-spacing:.2px}
.search{position:absolute;left:1059px;top:37px}
.welcome{position:absolute;left:50px;top:202px;font-size:51px;font-weight:300;letter-spacing:1px}
.hero-title{position:absolute;left:48px;top:285px;font-size:104px;line-height:92px;font-weight:900;font-style:italic;text-transform:uppercase;letter-spacing:-1px}

/* about */
.about{top:668px;height:827px;background:radial-gradient(ellipse at 50% 20%,#3a4766 0%,#26314b 50%,#1a2238 100%)}
.about .brand{left:50%;transform:translateX(-50%);top:72px}
.section-title{position:absolute;left:0;width:1200px;text-align:center;font-weight:700}
.about .section-title{top:152px;font-size:43px;letter-spacing:.3px}
.about-copy{position:absolute;left:195px;width:810px;top:230px;text-align:center;font-size:19px;line-height:25px}
.card{position:absolute;top:387px;width:238px;height:402px;background:var(--card);text-align:center;padding:0 18px}
.card svg{position:absolute;left:50%;transform:translateX(-50%);top:32px}
.card-label{position:absolute;left:0;right:0;top:120px;font-size:10px;font-weight:600}
.card-title{position:absolute;left:0;right:0;top:143px;font-size:19px;font-weight:700}
.card-body{position:absolute;left:24px;right:24px;top:182px;height:124px;overflow:hidden;font-size:12.5px;line-height:17.6px}
.btn-ghost{position:absolute;left:50%;transform:translateX(-50%);top:335px;width:97px;height:32px;background:var(--white);color:var(--red);font-size:12px;line-height:32px}
.arrow{position:absolute;width:40px;height:40px;border-radius:50%;display:flex;align-items:center;justify-content:center}
.arrow.light{background:var(--white)}
.arrow.dim{background:#d9dce3}

/* partners */
.partners{top:1495px;height:219px;background:linear-gradient(90deg,#2a1a14 0%,#7a3513 45%,#a24a17 70%,#3c2016 100%)}
.partners .section-title{top:30px;font-size:43px}
.partner{position:absolute;top:136px;font-size:26px;font-weight:800;letter-spacing:.5px}

/* rules */
.rules{top:1714px;height:469px;background:radial-gradient(ellipse at 50% 40%,#e6ebee 0%,#c7d0d6 60%,#aebac2 100%)}
.rules .section-title{top:30px;font-size:43px;color:var(--ink)}
.rule-tile{position:absolute;top:106px;width:234px;height:236px;display:flex;align-items:center;justify-content:center;font-size:38px;font-weight:800;text-shadow:0 2px 6px rgba(0,0,0,.5)}
.btn-solid{position:absolute;background:var(--red);color:var(--white);text-align:center}
.rules .btn-solid{left:534px;top:379px;width:133px;height:49px;line-height:49px;font-size:18px}

/* cta */
.cta{top:2183px;height:397px;background:radial-gradient(ellipse at 40% 75%,#6b3515 0%,#3a1d10 35%,#140d0b 75%)}
.cta .section-title{top:82px;font-size:36px}
.cta-copy{position:absolute;left:255px;width:690px;top:160px;text-align:center;font-size:14px;line-height:23px}
.cta .btn-solid{left:503px;top:257px;width:195px;height:50px;line-height:50px;font-size:18px}

/* footer */
.footer{top:2580px;height:272px;background:linear-gradient(180deg,#1e2740,#172036)}
.footer .brand{left:128px;top:93px;font-size:17px}
.copyright{position:absolute;left:123px;top:168px;font-size:12px}
.col-title{position:absolute;top:47px;font-size:20px;font-weight:700}
.contact-row{position:absolute;left:425px;display:flex;align-items:center;gap:12px;font-size:12px}
.link{position:absolute;left:684px;font-size:12px}
.social{position:absolute;left:956px;display:flex;align-items:center;gap:7px;font-size:12.5px}
.social-dot{width:26px;height:26px;border:1.5px solid var(--white);border-radius:50%}
</style>
</head>
<body>

<section class="hero">
  <div class="hero-photo" role="img" aria-label="Firefighter in full gear advancing through flames at night"></div>
  <div class="brand"><span class="brand-mark"></span>BLAZEGUARD RELAY</div>
  <nav class="nav"><span>ABOUT</span><span>OUR SERVICES</span><span>RULES &amp; PENALTIES</span><span>ENROLL NOW</span><span>FAQ</span></nav>
  <svg class="search" width="20" height="20" viewBox="0 0 20 20" fill="none" stroke="#fff" stroke-width="1.8"><circle cx="8.5" cy="8.5" r="6.5"/><line x1="13.5" y1="13.5" x2="18" y2="18"/></svg>
  <div class="welcome">WELCOME TO</div>
  <h1 class="hero-title">Blazeguard<br>Relay</h1>
</section>

<section class="about">
  <div class="brand"><span class="brand-mark"></span>BLAZEGUARD RELAY</div>
  <h2 class="section-title">ABOUT THE BLAZEGUARD RELAY</h2>
  <p class="about-copy">Lorem ipsum dolor sit amet, consectetur adipiscing elit, sed do eiusmod tempor incididunt ut labore et dolore magna aliqua. Quis ipsum suspendisse ultrices gravida. Risus commodo viverra maecenas accumsan lacus vel facilisis.</p>

  <div class="arrow dim" style="left:26px;top:593px"><svg width="14" height="14" viewBox="0 0 14 14" fill="none" stroke="#333" stroke-width="2"><polyline points="9,2 4,7 9,12"/></svg></div>
  <div class="arrow light" style="left:1126px;top:593px"><svg width="14" height="14" viewBox="0 0 14 14" fill="none" stroke="#222" stroke-width="2"><polyline points="5,2 10,7 5,12"/></svg></div>

  <article class="card" style="left:94px">
    <svg width="70" height="70" viewBox="0 0 70 70" fill="none" stroke="var(--blue)" stroke-width="4"><polyline points="4,66 4,54 20,54 20,40 36,40 36,26 52,26 52,6 66,6 66,66 4,66"/><line x1="12" y1="30" x2="26" y2="14"/><polyline points="16,14 26,14 26,24"/></svg>
    <div class="card-label">EVOLUTION:1</div>
    <h3 class="card-title">High-Rise Pack Carry</h3>
    <p class="card-body">It's the starting point of the course, where champions are born! Participants, waiting at the base of the tower, hear the alarm and begin their climb (run) up our 41 feet high, five (5) story tower of stairs (63 steps) carrying a 42lb hose pack. It's an ex-</p>
    <div class="btn-ghost">LEARN MORE</div>
  </article>
  <article class="card" style="left:352px">
    <svg width="70" height="70" viewBox="0 0 70 70" fill="none" stroke="var(--blue)" stroke-width="3"><circle cx="30" cy="30" r="26"/><circle cx="30" cy="30" r="18"/><circle cx="30" cy="30" r="10"/><circle cx="30" cy="30" r="3"/><path d="M56 30 V50"/><rect x="51" y="50" width="10" height="16"/></svg>
    <div class="card-label">EVOLUTION:2</div>
    <h3 class="card-title">The Hose Hoist</h3>
    <p class="card-body">Once at the top of the tower, participants will hand-over-hand hoist a 42lb donut roll of hose from the ground up to the top of the tower. It's mind over matter, working through the burn until the roll of hose clears the top</p>
    <div class="btn-ghost">LEARN MORE</div>
  </article>
  <article class="card" style="left:611px">
    <svg width="70" height="70" viewBox="0 0 70 70" fill="none" stroke="var(--blue)" stroke-width="3.5"><rect x="22" y="6" width="24" height="18" transform="rotate(45 34 15)"/><line x1="42" y1="26" x2="64" y2="48"/><rect x="6" y="56" width="34" height="8" rx="2"/></svg>
    <div class="card-label">EVOLUTION:3</div>
    <h3 class="card-title">Force Machine</h3>
    <p class="card-body">Presented by Kestrel®, participants will simulate a chopping motion using a 9.6lb dead blow hammer to force the 160lb Kestrel® Force Machine's steel beam a horizontal distance of 5 feet. Deep breath, you're half-way to the finish line!</p>
    <div class="btn-ghost">LEARN MORE</div>
  </article>
  <article class="card" style="left:868px">
    <svg width="70" height="70" viewBox="0 0 70 70" fill="none" stroke="var(--blue)" stroke-width="3"><rect x="22" y="4" width="14" height="8"/><rect x="16" y="12" width="26" height="52" rx="3"/><line x1="10" y1="30" x2="16" y2="30"/><path d="M42 34 H58 V64"/><line x1="52" y1="64" x2="64" y2="64"/></svg>
    <div class="card-label">EVOLUTION:4</div>
    <h3 class="card-title">The Hose Advance</h3>
    <p class="card-body">Participants will negotiate the 140-foot (42.6m) slalom course without missing or knocking over any delineator. They will then pick up the nozzle end of the 1-3/4 inch (4.45cm) charged hose line and drag it 75 feet. Once the nozzle penetrates the</p>
    <div class="btn-ghost">LEARN MORE</div>
  </article>
</section>

<section class="partners" role="img" aria-label="Smoke and fire glow behind the sponsor row">
  <h2 class="section-title">OUR PARTNERS</h2>
  <div class="arrow dim" style="left:26px;top:133px"><svg width="14" height="14" viewBox="0 0 14 14" fill="none" stroke="#333" stroke-width="2"><polyline points="9,2 4,7 9,12"/></svg></div>
  <div class="arrow light" style="left:1126px;top:133px"><svg width="14" height="14" viewBox="0 0 14 14" fill="none" stroke="#222" stroke-width="2"><polyline points="5,2 10,7 5,12"/></svg></div>
  <div class="partner" style="left:106px">Northwell Labs</div>
  <div class="partner" style="left:375px">Brightmark Gear</div>
  <div class="partner" style="left:680px">Kestrel</div>
  <div class="partner" style="left:934px">Quicklink Hose</div>
</section>

<section class="rules">
  <h2 class="section-title">Rules &amp; Penalties</h2>
  <div class="rule-tile" style="left:113px;background:linear-gradient(135deg,#5b1b1b,#2a2c33 60%,#4a4230)" role="img" aria-label="Firefighter with breathing tank seen from behind">RULE:1</div>
  <div class="rule-tile" style="left:359px;background:linear-gradient(135deg,#6a2a1a,#3a3a40 55%,#8a8d92)" role="img" aria-label="Firefighter in helmet and mask">RULE:2</div>
  <div class="rule-tile" style="left:605px;background:linear-gradient(135deg,#a3161c,#6a0f13 60%,#3c0a0c)" role="img" aria-label="Firefighter in red light holding a tool">RULE:3</div>
  <div class="rule-tile" style="left:851px;background:linear-gradient(135deg,#3d4a5e,#6a5a48 55%,#c9a55a)" role="img" aria-label="Firefighter kneeling with hose">RULE:4</div>
  <div class="btn-solid">View All</div>
</section>

<section class="cta" role="img" aria-label="Silhouetted firefighters against a dim fire glow">
  <h2 class="section-title">Surprise Yourself and Take the Challenge!</h2>
  <p class="cta-copy">It is a long established fact that a reader will be distracted by the readable content of a page when looking at its layout. The point of using Lorem Ipsum is that it has a more-or-less normal distribution of letters, as opposed to using 'Content here, content here',</p>
  <div class="btn-solid">ENROLL NOW</div>
</section>

<footer class="footer">
  <div class="brand"><span class="brand-mark"></span>BLAZEGUARD RELAY</div>
  <div class="copyright">©2023 All Rights Reserved</div>

  <div class="col-title" style="left:425px">CONTACT US</div>
  <div class="contact-row" style="top:87px"><svg width="20" height="22" viewBox="0 0 20 22" fill="none" stroke="#fff" stroke-width="1.5"><path d="M10 21 C4 14 3 11 3 8 a7 7 0 0 1 14 0 c0 3 -1 6 -7 13z"/><circle cx="10" cy="8" r="2.5"/></svg>P.O Box 412 Ember Lane 18</div>
  <div class="contact-row" style="top:124px"><svg width="22" height="22" viewBox="0 0 22 22" fill="none" stroke="#fff" stroke-width="1.5"><path d="M4 2 l4 0 2 5 -3 2 a12 12 0 0 0 6 6 l2 -3 5 2 0 4 a2 2 0 0 1 -2 2 A18 18 0 0 1 2 4 a2 2 0 0 1 2 -2z"/></svg>+(555) 014-2290</div>
  <div class="contact-row" style="top:163px"><svg width="22" height="16" viewBox="0 0 22 16" fill="none" stroke="#fff" stroke-width="1.5"><rect x="1" y="1" width="20" height="14"/><polyline points="1,1 11,9 21,1"/></svg>info@blazeguardrelay.example</div>
  <div class="contact-row" style="top:203px"><svg width="22" height="22" viewBox="0 0 22 22" fill="none" stroke="#fff" stroke-width="1.3"><circle cx="11" cy="11" r="10"/><ellipse cx="11" cy="11" rx="4.5" ry="10"/><line x1="1" y1="11" x2="21" y2="11"/><line x1="3" y1="6" x2="19" y2="6"/><line x1="3" y1="16" x2="19" y2="16"/></svg>www.blazeguardrelay.example</div>

  <div class="col-title" style="left:683px">COMPANY</div>
  <div class="link" style="top:93px">About Us</div>
  <div class="link" style="top:122px">Services</div>
  <div class="link" style="top:151px">Home</div>
  <div class="link" style="top:180px">Rules</div>
  <div class="link" style="top:210px">FAQ</div>

  <div class="col-title" style="left:956px">GET IN TOUCH</div>
  <div class="social" style="top:80px"><span class="social-dot"></span>Chirpline</div>
  <div class="social" style="top:121px"><span class="social-dot"></span>Facepage</div>
  <div class="social" style="top:159px"><span class="social-dot"></span>Worknet</div>
  <div class="social" style="top:200px"><span class="social-dot"></span>Snapgram</div>
</footer>

</body>
</html>
```